Mildwren.com infographic

We need an infographic that summarises the UK Budget (announced XX/XX) incomings (taxes) and outgoings (government expenditure).

We would be looking for a design that highlights the UK government debt compared with tax receipts in 2010 compared with 2009 if this could be fitted into one graphic.

Would be good to make pretty pictures of where the money is coming from and where it is being spent - if a comparison with 2009 isnt possible we will settle for just doing this for 2010 - though think a comparison to show the changes from 2009 to 2010 would be nice.

The graphic should be able to fit onto a 1280 x 768 px screen and still be readable.

Target Market(s)

35-60 year olds that are financially savvy and AB1

Industry/Entity Type

Graphic Design

Requirements
Must have
• The infographic must contain the ingoings and outgoings marked in bold on the attached document.
Nice to have
• a comparision of how this differs from 2009 to 2010 however will settle for an infographic focusing on the 2010 budget only if this is what time allows.
• ALSO - we need this by Monday morning 29th March latest.
Should not have
• offensive imagery

```html
<!DOCTYPE html>
<html lang="en">
<head>
<meta charset="utf-8">
<title>Mildwren.com – 2009 to 2010 Budget</title>
<link href="https://fonts.googleapis.com/css2?family=Lilita+One&family=Open+Sans:wght@700&family=Lato:wght@400;700&display=swap" rel="stylesheet">
<style>
  :root {
    --ink: #ffffff;
    --bg-deep: #0b0000;
    --bg-red: #a3000c;
    --bg-glow: #e0101e;
    --band-top: #ff1a1a;
    --band-bottom: #19b4f0;
    --heading-bar: #c4101a;
    --heading-bar-dark: #5a0008;
    --panel: #000000;
    --panel-edge: #d1141e;
    --label: #f2f2f2;
    --note: #bdbdbd;
    --budget-fill: #c9d4e4;
    --art-blue: #2b3f9a;
    --art-red: #d8173a;
  }
  html, body {
    margin: 0;
    padding: 0;
    width: 1200px;
    height: 720px;
    overflow: hidden;
    background: var(--bg-deep);
  }
  .canvas {
    position: relative;
    width: 1280px;
    height: 768px;
    transform: scale(0.9375);
    transform-origin: 0 0;
    overflow: hidden;
    background:
      radial-gradient(ellipse 620px 420px at 640px 230px, var(--bg-glow) 0%, var(--bg-red) 40%, #3a0004 78%, var(--bg-deep) 100%);
    font-family: "Lato", sans-serif;
  }
  .band-top { position: absolute; left: 0; top: 0; width: 1280px; height: 7px; background: var(--band-top); }
  .band-bottom { position: absolute; left: 0; bottom: 0; width: 1280px; height: 10px; background: var(--band-bottom); }

  .hero-art {
    position: absolute;
    left: 160px;
    top: 22px;
    width: 720px;
    height: 400px;
    border-radius: 46% 54% 40% 40% / 50% 50% 40% 40%;
    background:
      radial-gradient(ellipse 200px 180px at 120px 170px, var(--art-blue) 0%, rgba(43,63,154,0.6) 55%, transparent 75%),
      radial-gradient(ellipse 260px 150px at 470px 200px, #3450b8 0%, rgba(52,80,184,0.5) 55%, transparent 80%),
      radial-gradient(ellipse 260px 130px at 530px 90px, var(--art-red) 0%, rgba(216,23,58,0.4) 60%, transparent 85%);
  }

  .title { position: absolute; margin: 0; font-family: "Lilita One", sans-serif; font-weight: 400; line-height: 1; }
  .title-years { left: 664px; top: 62px; font-size: 66px; color: var(--ink); letter-spacing: 2px; }
  .title-year-new { left: 992px; top: 34px; font-size: 100px; color: var(--budget-fill); letter-spacing: 6px; text-shadow: 0 0 2px #6a7a90; }
  .title-budget { left: 1054px; top: 130px; font-size: 54px; color: var(--budget-fill); letter-spacing: 3px; text-shadow: 0 0 2px #6a7a90; }

  .section-heading {
    position: absolute;
    height: 37px;
    margin: 0;
    padding-left: 16px;
    box-sizing: border-box;
    border-radius: 8px;
    background: linear-gradient(90deg, var(--heading-bar) 0%, #b00c16 55%, var(--heading-bar-dark) 100%);
    color: var(--ink);
    font-family: "Open Sans", sans-serif;
    font-weight: 700;
    font-size: 25px;
    letter-spacing: 1.5px;
    line-height: 37px;
  }
  .heading-spending { left: 36px; top: 308px; width: 578px; }
  .heading-receipts { left: 668px; top: 308px; width: 578px; padding-left: 14px; }

  .chart-panel {
    position: absolute;
    top: 358px;
    width: 578px;
    height: 388px;
    box-sizing: border-box;
    border: 1px solid var(--panel-edge);
    border-radius: 6px;
    background: var(--panel);
  }
  .panel-spending { left: 36px; }
  .panel-receipts { left: 668px; }

  .charts { position: absolute; left: 0; top: 0; }
  .chart-total { font-family: "Lato", sans-serif; font-weight: 700; font-size: 13px; fill: var(--label); }
  .slice-label { font-family: "Lato", sans-serif; font-weight: 700; font-size: 11.5px; fill: var(--label); }
  .source-note { font-family: "Lato", sans-serif; font-size: 8px; fill: var(--note); }
</style>
</head>
<body>
<main class="canvas">
  <div class="band-top"></div>

  <div class="hero-art" role="img" aria-label="Illustration of a large pound sign in Union flag colours beside a pie chart topped with blue pound symbols"></div>

  <h1 class="title title-years">2009 to</h1>
  <p class="title title-year-new">2010</p>
  <p class="title title-budget">Budget</p>

  <h2 class="section-heading heading-spending">Government spending by function</h2>
  <h2 class="section-heading heading-receipts">Government receipt</h2>

  <section class="chart-panel panel-spending" aria-label="Government spending by function"></section>
  <section class="chart-panel panel-receipts" aria-label="Government receipts"></section>

  <svg class="charts" width="1280" height="768" viewBox="0 0 1280 768">
    <!-- Spending -->
    <text class="chart-total" x="72" y="388">Total managed expenditure: £671 billion</text>
    <g class="pie-spending" stroke="#000" stroke-width="0.6">
      <path d="M322 528 L322 420 A108 108 0 0 1 427.9 549.4 Z" fill="#e0533f"/>
      <path d="M322 528 L427.9 549.4 A108 108 0 0 1 417.4 578.7 Z" fill="#1e1e1e"/>
      <path d="M322 528 L417.4 578.7 A108 108 0 0 1 318.6 635.9 Z" fill="#b54a2a"/>
      <path d="M322 528 L318.6 635.9 A108 108 0 0 1 295.7 632.8 Z" fill="#5a5a5a"/>
      <path d="M322 528 L295.7 632.8 A108 108 0 0 1 227.3 579.9 Z" fill="#6e2a14"/>
      <path d="M322 528 L227.3 579.9 A108 108 0 0 1 215.1 543.6 Z" fill="#7a7a7a"/>
      <path d="M322 528 L215.1 543.6 A108 108 0 0 1 214.1 523.5 Z" fill="#4a1e10"/>
      <path d="M322 528 L214.1 523.5 A108 108 0 0 1 219.3 494.6 Z" fill="#141414"/>
      <path d="M322 528 L219.3 494.6 A108 108 0 0 1 235.5 463.3 Z" fill="#e8e4e4"/>
      <path d="M322 528 L235.5 463.3 A108 108 0 0 1 255.2 443.1 Z" fill="#3a1a10"/>
      <path d="M322 528 L255.2 443.1 A108 108 0 0 1 322 420 Z" fill="#4a4a4e"/>
    </g>
    <text class="slice-label" x="422" y="466">Social protection – £189bn</text>
    <text class="slice-label" x="438" y="561">Personal social</text>
    <text class="slice-label" x="438" y="577">services – £31bn</text>
    <text class="slice-label" x="370" y="635">Health – £119bn</text>
    <text class="slice-label" x="248" y="665">Transport – £23bn</text>
    <text class="slice-label" x="150" y="629">Education – £88bn</text>
    <text class="slice-label" x="138" y="591">Defence – £38bn</text>
    <text class="slice-label" x="96" y="546">Industry, agriculture,</text>
    <text class="slice-label" x="112" y="560">employment and</text>
    <text class="slice-label" x="120" y="574">training – £20bn</text>
    <text class="slice-label" x="120" y="513">Housing and</text>
    <text class="slice-label" x="91" y="527">environment – £29bn</text>
    <text class="slice-label" x="126" y="479">Public order and</text>
    <text class="slice-label" x="145" y="493">safety – £35bn</text>
    <text class="slice-label" x="136" y="448">Debt interest £28bn</text>
    <text class="slice-label" x="198" y="425">Other – £72bn</text>
    <g class="source-note">
      <text x="72" y="688">Source: Exchequer Office 2009-10 near-cash projections. Spending re-classified to functions compared to previous presentations and is</text>
      <text x="72" y="698">now using methods specified in international standards. Other expenditure includes spending on general public services: recreation,</text>
      <text x="72" y="708">culture, media and sport; international cooperation and development; public service pensions; plus spending yet to be allocated and</text>
      <text x="72" y="718">some accounting adjustments. Social protection includes tax credit payments in excess of an individual's tax liability, which are now</text>
      <text x="72" y="728">counted on AME, in line with OECD guidelines. Figures may not sum to total due to rounding.</text>
    </g>

    <!-- Receipts -->
    <text class="chart-total" x="692" y="387">Total receipts: £496 billion</text>
    <g class="pie-receipts" stroke="#000" stroke-width="0.6">
      <path d="M951 532 L951 417 A115 115 0 0 1 1063.4 556.5 Z" fill="#e0533f"/>
      <path d="M951 532 L1063.4 556.5 A115 115 0 0 1 964.2 646.2 Z" fill="#dedada"/>
      <path d="M951 532 L964.2 646.2 A115 115 0 0 1 901.9 636 Z" fill="#b54a2a"/>
      <path d="M951 532 L901.9 636 A115 115 0 0 1 862 604.8 Z" fill="#1e1e1e"/>
      <path d="M951 532 L862 604.8 A115 115 0 0 1 836.9 517.6 Z" fill="#6e2a14"/>
      <path d="M951 532 L836.9 517.6 A115 115 0 0 1 846.5 484.2 Z" fill="#888888"/>
      <path d="M951 532 L846.5 484.2 A115 115 0 0 1 866.5 453.9 Z" fill="#3a1a10"/>
      <path d="M951 532 L866.5 453.9 A115 115 0 0 1 951 417 Z" fill="#444448"/>
    </g>
    <text class="slice-label" x="1061" y="470">Income tax – £141bn</text>
    <text class="slice-label" x="1040" y="634">National Insurance – £98bn</text>
    <text class="slice-label" x="830" y="671">Excise duties – £44bn</text>
    <text class="slice-label" x="740" y="643">Corporation tax – £35bn</text>
    <text class="slice-label" x="766" y="579">VAT – £64bn</text>
    <text class="slice-label" x="698" y="509">Business rates – £24bn</text>
    <text class="slice-label" x="736" y="474">Council tax – £25bn</text>
    <text class="slice-label" x="808" y="426">Other – £67 bn</text>
    <g class="source-note">
      <text x="692" y="711">Source: Exchequer Office, 2009-10 projections. Other receipts include capital taxes, stamp duties, vehicle excise duties and some other</text>
      <text x="692" y="721">tax and non-tax receipts – for example, interest and dividends. Figures may not sum to total due to rounding.</text>
    </g>
  </svg>

  <div class="band-bottom"></div>
</main>
</body>
</html>
```